Simple : A Therapist is looking for a Design

Im lookind for a business card design for my new business .
my therapy field - Attuned Somatic Release .
Its part of Osteopatic medicine .
its gental, not invasive method that focus on the bones of the skull (cranial) .
i want some kind of skull in it like the attached photo.

Target Market(s)

people that suffer from pain

Industry/Entity Type

Physical Therapy

Contact Information for Business Card

i want people to understand this is diffrent kind of therapy
its anatomy base , gental and give outstanding result .

Font styles to use
Serif

Colors
fee18a
cadf82
fbc994
cedeed
fbe7d2
fff3d1

Requirements
Must have
• one side: my name (Eliran Tsabari) ,
• phone number ( 0541762908)
• email (tsabarieliran@mailvent.net)
• other side : Attuned Somatic Release
Nice to have
• i want some kind of skull in it like the attached photo.
• very powrful, accurate and smart.
• nice colores (maybe lite orange?, lite green?) , simple, relax, smart

```html
<!DOCTYPE html>
<html lang="en">
<head>
<meta charset="utf-8">
<title>Attuned Somatic Release — Business Card</title>
<link rel="stylesheet" href="https://fonts.googleapis.com/css2?family=Mulish:wght@400;700;800&display=swap">
<style>
  :root {
    --backdrop: #9c9c9c;
    --card-light: #f3f3f1;
    --card-orange: #f3bd86;
    --accent: #efa866;
    --ink: #4a4a4c;
    --white: #ffffff;
  }
  * { margin: 0; padding: 0; box-sizing: border-box; }
  html, body { width: 1200px; height: 720px; overflow: hidden; }
  body {
    background: var(--backdrop);
    font-family: "Mulish", Arial, sans-serif;
    display: flex;
    align-items: center;
    justify-content: center;
    gap: 40px;
  }
  .card {
    position: relative;
    width: 525px;
    height: 300px;
    box-shadow: 0 6px 18px rgba(0,0,0,0.25);
  }
  .card--front { background: var(--card-light); color: var(--ink); }
  .card--back { background: var(--card-orange); color: var(--white); }

  .brand {
    position: absolute;
    display: flex;
    align-items: center;
    gap: 14px;
    font-weight: 400;
    letter-spacing: 1px;
    white-space: nowrap;
  }
  .brand__dot {
    width: 44px; height: 44px;
    border-radius: 50%;
    flex: none;
  }
  .card--front .brand { left: 40px; top: 48px; font-size: 27px; color: var(--accent); }
  .card--front .brand__dot { background: var(--accent); }
  .card--back .brand { left: 50%; top: 50%; transform: translate(-50%, -50%); font-size: 29px; }
  .card--back .brand__dot { background: var(--white); }

  .holder-name {
    position: absolute;
    left: 40px; top: 138px;
    font-size: 25px;
    font-weight: 800;
    letter-spacing: 0.5px;
  }
  .contacts {
    position: absolute;
    left: 176px; top: 200px;
    list-style: none;
    font-size: 18px;
    letter-spacing: 1px;
  }
  .contacts li { display: flex; align-items: center; gap: 12px; margin-bottom: 12px; }
  .contacts__icon {
    width: 24px; height: 24px;
    border-radius: 50%;
    background: var(--accent);
    display: flex; align-items: center; justify-content: center;
    flex: none;
  }
</style>
</head>
<body>
  <section class="card card--front">
    <div class="brand">
      <span class="brand__dot"></span>
      <span class="brand__name">Attuned Somatic Release</span>
    </div>
    <h1 class="holder-name">Eliran Tsabari</h1>
    <ul class="contacts">
      <li>
        <span class="contacts__icon">
          <svg width="14" height="14" viewBox="0 0 24 24" aria-hidden="true"><path fill="#fff" d="M6.6 10.8a15.2 15.2 0 0 0 6.6 6.6l2.2-2.2c.3-.3.7-.4 1-.2 1.1.4 2.3.6 3.6.6.6 0 1 .4 1 1V20c0 .6-.4 1-1 1C10.6 21 3 13.4 3 4c0-.6.4-1 1-1h3.5c.6 0 1 .4 1 1 0 1.3.2 2.5.6 3.6.1.3 0 .7-.2 1z"/></svg>
        </span>
        <span>0541762908</span>
      </li>
      <li>
        <span class="contacts__icon">
          <svg width="14" height="14" viewBox="0 0 24 24" aria-hidden="true"><path fill="#fff" d="M3 6h18v12H3z"/><path fill="none" stroke="#efa866" stroke-width="1.8" d="M3 6l9 7 9-7"/></svg>
        </span>
        <span>tsabarieliran@mailvent.net</span>
      </li>
    </ul>
  </section>

  <section class="card card--back">
    <div class="brand">
      <span class="brand__dot"></span>
      <span class="brand__name">Attuned Somatic Release</span>
    </div>
  </section>
</body>
</html>
```